The Front Porch Playbook

I have a book that I need a cover for. The main title will be "The Greenvale Front Porch Playbook" and the secondary title will be "12 lessons from an open door" With the design, I think I'd like to include some sort of blueprint drawing with drafting like font. But the blueprint drawing isn't a requirement.

Target Market(s)

Home/property sellers

Industry/Entity Type

Real Estate

Font styles to use
Serif
Sans Serif
Other font styles liked:
• Architect type handwriting

```html
<!DOCTYPE html>
<html lang="en">
<head>
<meta charset="utf-8">
<title>The Greenvale Front Porch Playbook</title>
<link rel="stylesheet" href="https://fonts.googleapis.com/css2?family=Bebas+Neue&family=Open+Sans:wght@400;600&family=Yellowtail&display=swap">
<style>
  :root {
    --page: #ffffff;
    --cover-blue: #1f6db3;
    --cover-blue-deep: #17559a;
    --cover-blue-light: #3a8ad0;
    --drawing-line: #6fb0e6;
    --title-white: #ffffff;
    --accent-orange: #f5a300;
    --figure-white: #eef0f4;
    --figure-navy: #2a3a5c;
    --edge-shadow: rgba(10, 30, 60, 0.28);
  }
  html, body {
    margin: 0;
    padding: 0;
    width: 1200px;
    height: 1195px;
    overflow: hidden;
    background: var(--page);
  }
  .canvas {
    position: relative;
    width: 1200px;
    height: 1195px;
  }
  .book-cover {
    position: absolute;
    width: 800px;
    height: 1195px;
    overflow: hidden;
    transform-origin: 0 0;
    background: radial-gradient(ellipse at 50% 55%, var(--cover-blue-light) 0%, var(--cover-blue) 55%, var(--cover-blue-deep) 100%);
  }
  .book-cover--main {
    left: 0;
    top: 0;
  }
  .book-cover--small {
    left: 853px;
    top: 524px;
    transform: scale(0.343, 0.39);
    box-shadow: 20px 18px 40px var(--edge-shadow);
  }
  .title {
    position: absolute;
    left: 0;
    right: 0;
    top: 38px;
    margin: 0;
    text-align: center;
    font-family: "Bebas Neue", "Arial Narrow", sans-serif;
    font-weight: 400;
    color: var(--title-white);
    font-size: 150px;
    line-height: 122px;
    letter-spacing: 1px;
    text-transform: uppercase;
  }
  .title-line { display: block; }
  .title-script {
    position: absolute;
    left: 200px;
    top: 300px;
    font-family: "Yellowtail", "Brush Script MT", cursive;
    color: var(--accent-orange);
    font-size: 118px;
    line-height: 1;
    transform: rotate(-8deg);
  }
  .blueprint-drawing {
    position: absolute;
    left: 27px;
    top: 400px;
    width: 773px;
    height: 636px;
    border-radius: 40px;
    background: radial-gradient(ellipse at 50% 45%, rgba(111, 176, 230, 0.35) 0%, rgba(111, 176, 230, 0.12) 55%, rgba(111, 176, 230, 0) 80%);
  }
  .house-figurine {
    position: absolute;
    left: 304px;
    top: 571px;
    width: 229px;
    height: 359px;
    border-radius: 18px;
    background: linear-gradient(160deg, var(--figure-white) 0%, #c9cfdb 60%, var(--figure-navy) 100%);
    box-shadow: 0 20px 30px rgba(10, 30, 60, 0.35);
  }
  .subtitle {
    position: absolute;
    left: 49px;
    top: 1048px;
    display: flex;
    align-items: center;
    gap: 12px;
    margin: 0;
    font-family: "Open Sans", Arial, sans-serif;
    font-weight: 400;
    color: var(--title-white);
    font-size: 39px;
    text-transform: uppercase;
    white-space: nowrap;
  }
  .subtitle-number {
    display: inline-flex;
    align-items: center;
    justify-content: center;
    width: 76px;
    height: 76px;
    border-radius: 50%;
    background: var(--accent-orange);
    font-weight: 600;
    font-size: 38px;
  }
</style>
</head>
<body>
  <main class="canvas">
    <section class="book-cover book-cover--main">
      <div class="blueprint-drawing" role="img" aria-label="Faint architectural floor plan drawing in light blue lines"></div>
      <h1 class="title">
        <span class="title-line">The Greenvale</span>
        <span class="title-line">Front Porch</span>
      </h1>
      <div class="title-script">Playbook</div>
      <div class="house-figurine" role="img" aria-label="Small white and navy ceramic canal house figurine"></div>
      <p class="subtitle"><span class="subtitle-number">12</span><span class="subtitle-text">Lessons from an open door</span></p>
    </section>
    <section class="book-cover book-cover--small" aria-label="Book cover preview">
      <div class="blueprint-drawing" role="img" aria-label="Faint architectural floor plan drawing in light blue lines"></div>
      <p class="title">
        <span class="title-line">The Greenvale</span>
        <span class="title-line">Front Porch</span>
      </p>
      <div class="title-script">Playbook</div>
      <div class="house-figurine" role="img" aria-label="Small white and navy ceramic canal house figurine"></div>
      <p class="subtitle"><span class="subtitle-number">12</span><span class="subtitle-text">Lessons from an open door</span></p>
    </section>
  </main>
</body>
</html>
```